FUN and creative designs WANTED! Mobile Marketing Start-up Company

Website design needed.

- PO is a full service mobile marketing agency in existence to help connect companies with their audience on unwired devices (Smartphone and tablets).

- PO is a start-up business with no current website looking to make a solid, memorable first impression.
Updates

Please take into consideration the following two points from our brief:

-  sense of humour and fun. Showing that mobile marketing for your business can be easy, interesting, and not just for big companies.

- a little ‘left of centre’ (i.e. NOT corporate!)

Thanks!

Please don't use black as a back groud. 

Target Market(s)

Primarily Media Agencies and Direct clients of all business types

Industry/Entity Type

Marketing

Requirements
Must have
• •The website should be: simple, clean yet a little ‘left of centre’ (i.e. NOT corporate!)
•Colour-in-line with PO logo (Black, Grey and orange: RBG: 255, 59, 0)
•Font: Arial and Aller Bold as per logo
•The website needs to show the charter of the business- sense of humour and fun. Showing that mobile marketing for your business can be easy, interesting, and not just for big companies.

What pages are required:
-Home Page
-Why Mobile
-Why Pova
-Services
-Contact

* For initial submission only a home page and one sub-page is require as the other pages will work from the same template

* Coding would be great but not a essential
Nice to have
• Please suggest some stock photos for the website
Should not have
• Please review all attached documents:
* Full brief
* Logo files
* Web copy

```html
<!DOCTYPE html>
<html lang="en">
<head>
<meta charset="utf-8">
<title>Pova Labs – Why Mobile</title>
<link rel="stylesheet" href="https://fonts.googleapis.com/css2?family=Ubuntu:wght@400;500;700&family=Arimo:wght@400&display=swap">
<style>
  :root {
    --red: #d7464a;
    --cream: #fbefd7;
    --cream-light: #f9ebd2;
    --tan: #e4d4b3;
    --ink: #2b2a28;
    --green: #b8c24a;
    --footer: #343331;
    --footer-text: #ece0c4;
    --footer-muted: #bcb5a7;
    --link: #c9484b;
  }
  * { box-sizing: border-box; margin: 0; padding: 0; }
  html, body { width: 1200px; height: 870px; overflow: hidden; }
  body {
    position: relative;
    background: var(--cream);
    font-family: "Ubuntu", sans-serif;
    color: var(--ink);
  }

  .site-header { position: absolute; left: 0; top: 0; width: 1200px; height: 190px; }
  .band { position: absolute; left: 0; top: 0; }

  .brand {
    position: absolute; left: 160px; top: 52px;
    display: flex; align-items: center; gap: 16px;
    color: var(--ink); font-weight: 700;
  }
  .brand-dot { width: 52px; height: 52px; border-radius: 50%; background: var(--ink); }
  .brand-name { font-size: 70px; line-height: 70px; letter-spacing: 1px; }

  .main-nav { position: absolute; top: 40px; left: 580px; width: 540px; height: 100px; }
  .nav-item {
    position: absolute; top: 0; width: 120px; margin-left: -60px;
    text-align: center; text-decoration: none;
    color: var(--cream-light); font-weight: 700; font-size: 14px; letter-spacing: -.1px;
  }
  .nav-item .badge {
    display: block; width: 68px; height: 68px; margin: 0 auto 11px;
    border-radius: 50%; background: var(--cream-light);
  }
  .nav-item.is-active .badge { background: var(--green); }
  .nav-item .badge svg { width: 68px; height: 68px; display: block; }

  .page-title {
    position: absolute; left: 156px; top: 219px;
    font-size: 39px; font-weight: 700; letter-spacing: -1.2px; line-height: 48px;
  }
  .intro {
    position: absolute; left: 158px; top: 270px;
    font-size: 14px; line-height: 20px; letter-spacing: -.2px; white-space: nowrap;
  }
  .block { position: absolute; white-space: nowrap; }
  .block h2 { font-size: 18.5px; font-weight: 700; letter-spacing: -.3px; line-height: 24px; margin-bottom: 0; }
  .block p { font-size: 12.2px; line-height: 19.6px; letter-spacing: -.2px; }
  .block-wide { left: 158px; top: 408px; }
  .block-col-1 { left: 158px; top: 555px; }
  .block-col-2 { left: 439px; top: 555px; }
  .highlight {
    position: absolute; left: 743px; top: 538px; width: 310px; height: 135px;
    background: var(--tan); border-radius: 14px;
  }
  .block-col-3 { left: 764px; top: 555px; }

  .mascot {
    position: absolute; left: 740px; top: 228px; width: 335px; height: 310px;
    border-radius: 46% 46% 30% 30%;
    background: radial-gradient(circle at 62% 40%, #f4efcf 0 32%, #cdd27a 55%, rgba(251,239,215,0) 72%);
  }

  .site-footer { position: absolute; left: 0; top: 696px; width: 1200px; height: 174px; }
  .footer-col { position: absolute; top: 46px; color: var(--footer-text); }
  .footer-col h3 { font-weight: 400; font-size: 19.5px; line-height: 26px; margin-bottom: 8px; display: flex; align-items: center; gap: 12px; }
  .footer-col h3 .dot { width: 20px; height: 20px; border-radius: 50%; background: var(--footer-text); }
  .footer-col p { font-family: "Arimo", sans-serif; font-size: 14px; line-height: 20px; color: var(--footer-muted); }
  .footer-col a { color: var(--link); text-decoration: none; font-family: "Arimo", sans-serif; font-size: 14px; }
  .feed { left: 152px; }
  .contact { left: 646px; }
  .connect { left: 878px; }
  .social { display: flex; gap: 7px; margin-top: 2px; }
  .social a {
    width: 41px; height: 41px; border-radius: 5px;
    background: #262524; border: 1px solid #4a4845;
    display: flex; align-items: center; justify-content: center;
  }
  .social a span { width: 16px; height: 16px; border-radius: 50%; background: var(--footer-text); }
</style>
</head>
<body>

<header class="site-header">
  <svg class="band" width="1200" height="190" viewBox="0 0 1200 190" aria-hidden="true">
    <path fill="#d7464a" d="M0 0H1200V186L1160 182 1120 187 1060 181 990 186 920 180 860 185 790 181 720 187 650 181 580 186 510 180 440 186 370 181 300 187 230 181 160 186 90 180 40 186 0 181Z"/>
    <path fill="#2d2b29" d="M0 0H1200V8L1150 12 1080 6 1000 11 930 5 860 10 780 6 700 12 620 6 540 11 460 5 380 10 300 6 220 12 140 6 60 11 0 7Z"/>
  </svg>

  <div class="brand">
    <span class="brand-dot"></span>
    <span class="brand-name">Pova</span>
  </div>

  <nav class="main-nav">
    <a class="nav-item" href="#" style="left:36px">
      <span class="badge"><svg viewBox="0 0 68 68"><path d="M20 44L34 22 48 44Z" fill="#cf3c40"/></svg></span>HOME
    </a>
    <a class="nav-item is-active" href="#" style="left:146px">
      <span class="badge"><svg viewBox="0 0 68 68"><rect x="25" y="18" width="18" height="32" rx="3" fill="none" stroke="#cf3c40" stroke-width="3"/><circle cx="34" cy="45" r="1.8" fill="#cf3c40"/></svg></span>WHY MOBILE
    </a>
    <a class="nav-item" href="#" style="left:248px">
      <span class="badge"><svg viewBox="0 0 68 68"><circle cx="24" cy="44" r="4" fill="#cf3c40"/><path d="M24 33a11 11 0 0 1 11 11M24 24a20 20 0 0 1 20 20" fill="none" stroke="#cf3c40" stroke-width="4"/></svg></span>WHY POVA
    </a>
    <a class="nav-item" href="#" style="left:361px">
      <span class="badge"><svg viewBox="0 0 68 68"><path d="M21 35L30 44 48 24" fill="none" stroke="#cf3c40" stroke-width="5" stroke-linecap="round" stroke-linejoin="round"/></svg></span>SERVICES
    </a>
    <a class="nav-item" href="#" style="left:474px">
      <span class="badge"><svg viewBox="0 0 68 68"><path d="M38 15L24 38H33L28 54 45 29H36Z" fill="#cf3c40"/></svg></span>CONTACT
    </a>
  </nav>
</header>

<main>
  <h1 class="page-title">Why Mobile</h1>
  <p class="intro">Lorem ipsum dolor sit amet, consectetur adipisicing elit, sed do eiusmod tempor<br>incididunt ut labore et dolore magna aliqua. Ut enim ad minim veniam, quis nostrud<br>exercitation ullamco laboris nisi ut aliquip ex ea commodo consequat. Duis aute irure<br>dolor in reprehenderit in voluptate velit esse cillum dolore eu fugiat nulla pariatur.<br>Excepteur sint occaecat cupidatat non proident, sunt in culpa qui officia deserunt<br>mollit anim id est laborum.</p>

  <section class="block block-wide">
    <h2>Sub Header</h2>
    <p>Lorem ipsum dolor sit amet, consectetur adipisicing elit, sed do eiusmod tempor incididunt ut<br>labore et dolore magna aliqua. Ut enim ad minim veniam, quis nostrud exercitation ullamco laboris<br>nisi ut aliquip ex ea commodo consequat. Duis aute irure dolor in reprehenderit in voluptate velit<br>esse cillum dolore eu fugiat nulla pariatur. Excepteur sint occaecat cupidatat non proident, sunt in<br>culpa qui officia deserunt mollit anim id est laborum.</p>
  </section>

  <div class="mascot" role="img" aria-label="Illustration of a cheerful round robot mascot with antennae and green sneakers, holding a tablet"></div>

  <section class="block block-col-1">
    <h2>Sub Header</h2>
    <p>Lorem ipsum dolor sit amet, consectetur adipisi<br>cing elit, sed do eiusmod tempor incididunt ut<br>labore et dolore magna aliqua. Ut enim ad mi<br>nim veniam, quis nostrud exercitation ullamco</p>
  </section>
  <section class="block block-col-2">
    <h2>Sub Header</h2>
    <p>Lorem ipsum dolor sit amet, consectetur adipisi<br>cing elit, sed do eiusmod tempor incididunt ut<br>labore et dolore magna aliqua. Ut enim ad mi<br>nim veniam, quis nostrud exercitation ullamco</p>
  </section>
  <div class="highlight"></div>
  <section class="block block-col-3">
    <h2>Sub Header</h2>
    <p>Lorem ipsum dolor sit amet, consectetur adipisi<br>cing elit, sed do eiusmod tempor incididunt ut<br>labore et dolore magna aliqua. Ut enim ad mi<br>nim veniam, quis nostrud exercitation ullamco</p>
  </section>
</main>

<footer class="site-footer">
  <svg class="band" width="1200" height="174" viewBox="0 0 1200 174" aria-hidden="true">
    <path fill="#343331" d="M0 6L50 2 120 7 190 1 260 6 330 2 400 8 470 2 540 6 610 1 680 7 750 2 820 6 890 1 960 7 1030 2 1100 6 1160 1 1200 5V174H0Z"/>
  </svg>

  <div class="footer-col feed">
    <h3>@PovaLabs on Chatter <span class="dot"></span></h3>
    <p>Pova Labs @PovaLabs</p>
    <p>More smartphone revolution. Will lumio and panes fight back?</p>
    <a href="#">go.brief.li/k7Qa2</a>
  </div>

  <div class="footer-col contact">
    <h3>contact us</h3>
    <p>info@povalabs.com</p>
    <p>1.800.555.014</p>
  </div>

  <div class="footer-col connect">
    <h3>connect with us</h3>
    <div class="social">
      <a href="#" aria-label="Facepage"><span></span></a>
      <a href="#" aria-label="Chatter"><span></span></a>
    </div>
  </div>
</footer>

</body>
</html>
```